The Marwick Doctrines book cover design [front and back covers]

I need a book cover design for a trade book called THE MARWICK DOCTRINES.

Cover Title: the Marwick Doctrines
Subheading: The business wisdom of Colin Marwick, a successful Australian entrepreneur.

NOTE: I originally posted this contest with 2 authors. I NOW ONLY WANT TO HAVE ONE AUTHORS NAME ON THE BOOK. Author: Colin Marwick

It's about the business principals that has made this man so successful.

The man this book is about owns a company called Tallow Rentals and their colour is red. So I'd like the cover to have a strong red influence. I've included his logo and other samples of their branding.

I'd like the book design to look like a Brindle Weekly Ledger best seller style book. Sophisticated and simple. I'd like it to be clear that this book comes from the same man that built Tallow rentals, but I don't want it to look like a corporate brochure. It must look like a book you would see at the airport book shop.

I've also included some book cover inspiration to give you an idea of the direction I'd like for this design.

```html
<!DOCTYPE html>
<html lang="en">
<head>
<meta charset="utf-8">
<title>The Marwick Doctrines – Book Cover</title>
<link rel="stylesheet" href="https://fonts.googleapis.com/css2?family=Tinos:wght@400;700&family=Arimo:wght@700&display=swap">
<style>
  :root {
    --backdrop: #c8c8c8;
    --cover-red: #cc0c0c;
    --ornament-red: #b50909;
    --ink-white: #ffffff;
    --ink-soft: #f1e4e4;
  }
  * { margin: 0; padding: 0; box-sizing: border-box; }
  html, body {
    width: 1200px;
    height: 1200px;
    overflow: hidden;
    background: var(--backdrop);
  }
  .canvas {
    position: relative;
    width: 1200px;
    height: 1200px;
  }
  .book-cover {
    position: absolute;
    left: 257px;
    top: 84px;
    width: 686px;
    height: 1032px;
    background: var(--cover-red);
    color: var(--ink-white);
    text-align: center;
  }
  .flourish {
    position: absolute;
    left: 235px;
    top: 96px;
    width: 192px;
    height: 60px;
    border-radius: 50%;
    background: radial-gradient(ellipse at center, var(--ornament-red) 0%, var(--cover-red) 70%);
  }
  .title-rule {
    position: absolute;
    height: 3px;
    background: var(--ink-white);
  }
  .title-rule--left { left: 62px; top: 355px; width: 190px; }
  .title-rule--right { left: 437px; top: 355px; width: 187px; }
  .title-rule--base { left: 62px; top: 569px; width: 562px; }
  .title {
    font-family: "Tinos", "Times New Roman", serif;
    font-weight: 400;
    line-height: 1;
  }
  .title-line {
    position: absolute;
    left: 0;
    width: 100%;
    white-space: nowrap;
  }
  .title-line--the { top: 287px; font-size: 98px; }
  .title-line--name {
    top: 371px;
    font-size: 114px;
    transform: scaleY(1.14);
    transform-origin: center top;
  }
  .title-line--doctrines { top: 474px; font-size: 97px; }
  .subtitle {
    position: absolute;
    left: 62px;
    top: 583px;
    width: 562px;
    font-family: "Arimo", Arial, sans-serif;
    font-weight: 700;
    font-size: 19px;
    line-height: 1.2;
  }
  .author {
    position: absolute;
    left: 0;
    top: 915px;
    width: 100%;
    font-family: "Tinos", "Times New Roman", serif;
    font-weight: 700;
    font-size: 32px;
    color: var(--ink-soft);
  }
</style>
</head>
<body>
  <main class="canvas">
    <section class="book-cover">
      <div class="flourish" role="img" aria-label="Decorative calligraphic flourish"></div>

      <div class="title-rule title-rule--left"></div>
      <div class="title-rule title-rule--right"></div>
      <h1 class="title">
        <span class="title-line title-line--the">THE</span>
        <span class="title-line title-line--name">MARWICK</span>
        <span class="title-line title-line--doctrines">DOCTRINES</span>
      </h1>
      <div class="title-rule title-rule--base"></div>

      <p class="subtitle">The business wisdom of Colin Marwick, a successful<br>Australian entrepreneur.</p>

      <p class="author">Colin Marwick</p>
    </section>
  </main>
</body>
</html>
```